Modern Medical Optometry Website

We need mordern, Patient friendly website. Easy to navigate and enhance our advance medical technology and excellent patient care.
1. HOME PAGE
2. OUR TEAM PAGE
3. EYECARE PAGE - VISION SERVICES, EYE EXAMS, KERATOCONUS CENTER, GLAUCOMA , DIABITES, TORVANEX EXAM, DIGITAL RETINAL, OCT.
4. MYOPIA CONTROL CLINIC
5. DRY EYE CLINIC
6. EYEWEAR
7. PATIENT CENTER - BLOG
7. CONTACT US
This is our current website www.brindlecove.com
and We want to add more content and a cleaner design like these website
http://tamsworthoptometry.com/
https://www.klmhaven.com/

```html
<!DOCTYPE html>
<html lang="en">
<head>
<meta charset="utf-8">
<title>Brindle Cove Optometry</title>
<link rel="stylesheet" href="https://fonts.googleapis.com/css2?family=Montserrat:wght@400;500;600;700&family=Open+Sans:wght@400;600&family=Merriweather:wght@400&display=swap">
<style>
:root{
  --blue:#4a86e0;
  --yellow:#f5c416;
  --yellow-deep:#f0b40c;
  --ink:#2b2e34;
  --ink-soft:#34383f;
  --grey:#7a7f88;
  --purple:#9b8ce6;
  --white:#ffffff;
  --sky:#e9f1f8;
}
*{box-sizing:border-box;margin:0;padding:0}
html,body{width:1200px;height:3711px;overflow:hidden}
body{font-family:"Open Sans",Arial,sans-serif;color:var(--ink);background:var(--white);position:relative}
section,header,footer{position:absolute;left:0;width:1200px}
.abs{position:absolute}
.pill{display:inline-block;border-radius:30px;font-family:"Montserrat",Arial,sans-serif;font-size:10px;letter-spacing:1px;text-transform:uppercase;text-align:center}
.pill-outline-white{border:1.5px solid var(--white);color:var(--white);padding:7px 22px}

/* hero */
.hero{top:0;height:638px;background:linear-gradient(180deg,#ffffff 0%,#f6f9fc 55%,var(--sky) 100%)}
.brand{left:55px;top:20px;width:180px;text-align:center}
.brand-mark{width:46px;height:46px;border-radius:50%;background:var(--yellow);margin:0 auto 8px}
.brand-name{font-family:"Montserrat",Arial,sans-serif;font-size:19px;font-weight:500;color:var(--ink-soft);letter-spacing:1px;line-height:1.1;white-space:nowrap}
.brand-sub{font-family:"Montserrat",Arial,sans-serif;font-size:10px;color:var(--ink-soft);line-height:1.2}
.callout{left:630px;top:50px;font-size:13px;color:var(--grey)}
.callout b{color:var(--yellow-deep);font-weight:600}
.appt-btn{left:885px;top:40px;width:186px;height:38px;line-height:38px;background:var(--blue);color:var(--white);border-radius:20px;font-family:"Montserrat",Arial,sans-serif;font-size:11px;font-weight:600;text-align:center}
.flag{left:1097px;top:50px;width:18px;height:18px;border-radius:50%;background:linear-gradient(180deg,#c8333f 50%,#2f4d9a 50%)}
.nav{left:396px;top:121px;display:flex;font-family:"Montserrat",Arial,sans-serif;font-size:11px;color:var(--grey)}
.nav span{margin-right:37px}
.nav .active{color:var(--blue)}
.hero-title{left:148px;top:292px;font-family:"Montserrat",Arial,sans-serif;font-size:36px;font-weight:600;color:var(--yellow);line-height:1.15;width:340px}
.hero-text{left:148px;top:380px;width:320px;font-size:12.5px;line-height:1.55;color:var(--grey)}
.hero-btn{left:148px;top:458px;border:1.5px solid var(--purple);color:var(--purple);padding:7px 22px}
.device{left:655px;top:195px;width:380px;height:430px;border-radius:40px 40px 20px 20px;background:linear-gradient(160deg,#f3f4f6 0%,#d8dadd 60%,#b9bcc1 100%)}

/* promise */
.promise{top:638px;height:411px}
.promise-photo{left:0;top:0;width:600px;height:411px;background:linear-gradient(135deg,#e9ddd3 0%,#c9a98d 55%,#b85c4c 100%)}
.promise-panel{left:600px;top:0;width:600px;height:411px;background:var(--blue);color:var(--white)}
.promise-panel h2{position:absolute;left:75px;top:92px;font-family:"Montserrat",Arial,sans-serif;font-size:20px;font-weight:700;color:var(--yellow)}
.promise-panel h3{position:absolute;left:75px;top:120px;font-family:"Montserrat",Arial,sans-serif;font-size:17px;font-weight:600}
.promise-panel p{position:absolute;left:75px;top:160px;width:450px;font-size:11.5px;line-height:1.6;opacity:.92}
.promise-panel .pill{position:absolute;left:75px;top:284px}

/* services */
.services{top:1049px;height:299px;display:flex}
.tile{position:relative;width:300px;height:299px}
.tile span{position:absolute;left:0;right:0;top:140px;text-align:center;font-family:"Montserrat",Arial,sans-serif;font-size:15px;letter-spacing:2px;color:var(--white);text-transform:uppercase}
.tile-exams{background:linear-gradient(135deg,#c9ccd0,#8d6f5d)}
.tile-eyewear{background:linear-gradient(135deg,#55575a,#2e3033)}
.tile-dry{background:linear-gradient(135deg,#aeb3b9,#4f5358)}
.tile-lenses{background:linear-gradient(135deg,#c6d6e1,#7f9db1)}

/* insurance */
.insurance{top:1348px;height:414px;background:var(--blue)}
.insurance h2{position:absolute;left:148px;top:96px;font-family:"Montserrat",Arial,sans-serif;font-size:20px;font-weight:700;color:var(--yellow)}
.insurance h3{position:absolute;left:148px;top:122px;font-family:"Montserrat",Arial,sans-serif;font-size:16px;font-weight:600;color:var(--white)}
.insurance p{position:absolute;left:148px;top:160px;width:350px;font-size:11.5px;line-height:1.6;color:var(--white);opacity:.92}
.insurance .pill{position:absolute;left:148px;top:264px}
.chart-photo{left:600px;top:0;width:300px;height:414px;background:linear-gradient(150deg,#f2f4f7 0%,#dfe3ea 60%,#5f86c9 100%)}

/* review */
.review{top:1762px;height:633px}
.review-left{left:0;top:0;width:300px;height:633px;background:linear-gradient(160deg,#e7eaee,#a9b0b9)}
.review-right{left:300px;top:0;width:900px;height:633px;background:linear-gradient(120deg,#eef0f2 0%,#c8ccd1 45%,#6f6259 100%)}
.review-card{left:300px;top:0;width:300px;height:410px;background:var(--ink);color:var(--white)}
.source-dot{position:absolute;left:137px;top:26px;width:26px;height:26px;border-radius:50%;background:#d9d9d9}
.meta{position:absolute;left:0;right:0;top:64px;text-align:center;font-size:10px;color:#c9ccd1}
.meta b{color:var(--yellow);letter-spacing:1px;font-weight:400}
.quote{position:absolute;left:38px;top:92px;width:228px;font-family:"Merriweather",Georgia,serif;font-size:12.5px;line-height:1.75;color:#e9eaec}
.author{position:absolute;left:0;right:0;top:330px;text-align:center;font-family:"Merriweather",Georgia,serif;font-size:11.5px;color:#b9bcc2}
.avatar{left:420px;top:380px;width:60px;height:60px;border-radius:50%;background:#b9a99a;border:3px solid var(--white)}
.dots{left:410px;top:522px;display:flex;gap:6px}
.dots i{width:8px;height:8px;border-radius:50%;border:1px solid var(--white);display:block}
.dots i.on{background:var(--white)}

/* team */
.team{top:2395px;height:415px;display:flex}
.member{position:relative;width:300px;height:415px;background:linear-gradient(180deg,var(--yellow) 0%,var(--yellow-deep) 100%)}
.member-photo{position:absolute;left:55px;top:70px;width:190px;height:345px;border-radius:95px 95px 0 0;background:linear-gradient(180deg,#3a3230 0%,#d7b39c 35%,#f4f5f7 70%)}
.member.dark .member-photo{background:linear-gradient(180deg,#2c2622 0%,#bfa083 35%,#eadfc7 70%)}
.member.blue .member-photo{background:linear-gradient(180deg,#201c1b 0%,#c9a28a 32%,#dfe4ee 62%,#4d5e86 100%)}
.member.focus{background:linear-gradient(180deg,#e6c23a 0%,#d7b232 100%)}
.member.focus .member-photo{background:linear-gradient(180deg,#3b3327 0%,#a88d4e 35%,#7d6a35 70%,#6e5d2e 100%)}
.member-name{position:absolute;left:0;right:0;text-align:center;font-family:"Montserrat",Arial,sans-serif;font-size:15px;font-weight:700;color:var(--ink)}
.member-role{position:absolute;left:0;right:0;text-align:center;font-size:9.5px;color:var(--ink)}
.member.focus .member-name,.member.focus .member-role{color:var(--white)}
.more{position:absolute;left:96px;top:350px;width:108px;height:28px;line-height:28px;background:var(--purple);color:var(--white);border-radius:15px;font-family:"Montserrat",Arial,sans-serif;font-size:9.5px;letter-spacing:1px;text-align:center;text-transform:uppercase}

/* contact bar */
.contact-bar{top:2810px;height:149px;background:var(--blue);color:var(--white)}
.contact-item{position:absolute;top:46px;width:220px;text-align:center;font-family:"Montserrat",Arial,sans-serif;font-size:13px}
.contact-item svg{display:block;margin:0 auto 12px}

/* map */
.map{top:2959px;height:413px;background:linear-gradient(180deg,#eceae6,#e3e1dc)}

/* footer */
.footer{top:3372px;height:339px;background:var(--ink-soft);color:#d4d6da;display:flex}
.fcol{position:relative;width:300px;height:339px;border-right:1px solid #454a52;text-align:center}
.fcol:last-child{border-right:none}
.fcol h4{position:absolute;left:0;right:0;top:82px;font-family:"Montserrat",Arial,sans-serif;font-size:13px;font-weight:600;color:var(--white)}
.fcol .addr{position:absolute;left:0;right:0;top:104px;font-size:10.5px;line-height:1.5;color:#b9bcc2}
.fcol .lines{position:absolute;left:0;right:0;top:158px;font-size:10.5px;line-height:1.6;color:#b9bcc2}
.fcol .pill{position:absolute;left:96px;top:216px;width:108px;border:1.5px solid #6f7580;color:#c9ccd1;padding:7px 0}
.pin{position:absolute;left:128px;top:-22px;width:44px;height:44px;border-radius:50%}
.pin svg{display:block;margin:12px auto 0}
.foot-brand{position:absolute;left:0;right:0;top:45px}
.foot-brand .brand-name{color:var(--white);font-size:21px}
.foot-brand .brand-sub{color:#c9ccd1}
.copy{position:absolute;left:0;right:0;top:232px;font-size:9.5px;color:#b9bcc2}
.socials{position:absolute;left:0;right:0;top:110px;display:flex;justify-content:center;gap:8px}
.socials i{width:24px;height:24px;border-radius:50%;display:block}
.contact-link{position:absolute;left:0;right:0;top:232px;font-size:9.5px;color:#b9bcc2}
</style>
</head>
<body>

<header class="hero">
  <div class="abs brand">
    <div class="brand-mark"></div>
    <div class="brand-name">BRINDLE COVE</div>
    <div class="brand-sub">Optometry</div>
  </div>
  <div class="abs callout">Call or Text Us: <b>818 . 555 . 0142</b></div>
  <div class="abs appt-btn">Make An Appointment</div>
  <div class="abs flag"></div>
  <nav class="abs nav">
    <span class="active">[ Home ]</span><span>About</span><span>Services</span><span>Eyewear</span><span>Dry Eye Clinic</span><span>Patient Centre</span><span>Promotions</span><span>Reviews</span>
  </nav>
  <h1 class="abs hero-title">No Air Puffs. No Eye Drops</h1>
  <p class="abs hero-text">Dedicated to the highest level of service, we provide patient friendly eye exams with no air puffs and no eye drops.</p>
  <div class="abs pill hero-btn">More Info</div>
  <div class="abs device" role="img" aria-label="Handheld tonometer device floating above soft clouds"></div>
</header>

<section class="promise">
  <div class="abs promise-photo" role="img" aria-label="Mother and daughter playing with an eye exam occluder"></div>
  <div class="abs promise-panel">
    <h2>The Brindle Cove Promise</h2>
    <h3>Healthy Eyesight</h3>
    <p>Welcome to Brindle Cove Optometry, where your vision and eye health are our sole priority. We take great pride in providing you with state-of-the-art eyecare matched with personal attention from our staff and doctors. Your quality of life is our goal and we believe that healthy eyesight is vital to achieving it.</p>
    <div class="pill pill-outline-white">About Us</div>
  </div>
</section>

<section class="services">
  <div class="tile tile-exams" role="img" aria-label="Child trying on trial frames during an eye exam"><span>Exams</span></div>
  <div class="tile tile-eyewear" role="img" aria-label="Eyeglasses on a dark surface"><span>Eye Wear</span></div>
  <div class="tile tile-dry" role="img" aria-label="Woman rubbing tired dry eyes"><span>Dry Eyes</span></div>
  <div class="tile tile-lenses" role="img" aria-label="Contact lenses close up"><span>Lenses</span></div>
</section>

<section class="insurance">
  <h2>Insurance</h2>
  <h3>Health / Vision Insurance</h3>
  <p>Lorem ipsum dolor sit amet, consectetur adipiscing elit, sed do eiusmod tempor incididunt ut labore et dolore magna aliqua. Ut enim ad minim veniam, quis nostrud exercitation ullamco laboris nisi ut aliquip ex ea commodo.</p>
  <div class="pill pill-outline-white">Learn More</div>
  <div class="abs chart-photo" role="img" aria-label="Eyeglasses resting on an eye chart beside a small plant"></div>
</section>

<section class="review">
  <div class="abs review-left" role="img" aria-label="Examination equipment in soft focus"></div>
  <div class="abs review-right" role="img" aria-label="Patient looking into a slit lamp microscope with the optometrist"></div>
  <div class="abs review-card">
    <div class="source-dot"></div>
    <div class="meta"><b>★★★★★</b> &nbsp;3 weeks ago</div>
    <p class="quote">Love this place to death! I've been going for a few years and everyone there is so nice and inform patients of their procedures. They are bilingual in Vietnamese and English which is awesome. Not to mention all the staff are pretty nice and kind! Shoutout to Dr. Vell and Dr. Soto. Of course to Felix too! Great people and great ...</p>
    <div class="author">- Marcus Dunn -</div>
  </div>
  <div class="abs avatar" role="img" aria-label="Reviewer portrait"></div>
  <div class="abs dots"><i class="on"></i><i></i><i></i><i></i><i></i></div>
</section>

<section class="team">
  <div class="member">
    <div class="member-photo" role="img" aria-label="Portrait of Dr. Nora Vell"></div>
    <div class="member-name" style="top:322px">Dr. Nora Vell, O.D.</div>
    <div class="member-role" style="top:344px">(Optometrist)</div>
  </div>
  <div class="member focus">
    <div class="member-photo" role="img" aria-label="Portrait of Dr. Irene Calder"></div>
    <div class="member-name" style="top:300px">Dr. Irene Calder</div>
    <div class="member-role" style="top:322px">(Associate Doctor)</div>
    <div class="more">More Info</div>
  </div>
  <div class="member dark">
    <div class="member-photo" role="img" aria-label="Portrait of Dr. Maya Torrens"></div>
    <div class="member-name" style="top:322px">Dr. Maya Torrens</div>
    <div class="member-role" style="top:344px">(Associate Doctor)</div>
  </div>
  <div class="member blue">
    <div class="member-photo" role="img" aria-label="Portrait of Owen L."></div>
    <div class="member-name" style="top:322px">Owen L.</div>
    <div class="member-role" style="top:344px">(Office Manager)</div>
  </div>
</section>

<section class="contact-bar">
  <div class="contact-item" style="left:206px">
    <svg width="30" height="30" viewBox="0 0 24 24" fill="none" stroke="#fff" stroke-width="1.6" stroke-linejoin="round"><path d="M5 3h4l2 5-2.5 1.5a11 11 0 0 0 6 6L16 13l5 2v4a2 2 0 0 1-2 2A16 16 0 0 1 3 5a2 2 0 0 1 2-2z"/></svg>
    818 . 555 . 0142
  </div>
  <div class="contact-item" style="left:490px">
    <svg width="30" height="30" viewBox="0 0 24 24" fill="none" stroke="#fff" stroke-width="1.6"><rect x="3" y="5" width="18" height="16" rx="2"/><path d="M3 10h18M8 3v4M16 3v4M9 15l2 2 4-4"/></svg>
    Make An Appointment
  </div>
  <div class="contact-item" style="left:793px">
    <svg width="30" height="30" viewBox="0 0 24 24" fill="none" stroke="#fff" stroke-width="1.6"><path d="M6 2h9l4 4v16H6z"/><path d="M15 2v4h4M9 11h7M9 15h7M9 19h5"/></svg>
    Patient Forms
  </div>
</section>

<section class="map" role="img" aria-label="Street map showing the clinic location"></section>

<footer class="footer">
  <div class="fcol">
    <div class="foot-brand">
      <div class="brand-mark"></div>
      <div class="brand-name">BRINDLE COVE</div>
      <div class="brand-sub">Optometry</div>
    </div>
    <div class="copy">Brindle Cove Optometry © 2019</div>
  </div>
  <div class="fcol">
    <div class="pin" style="background:var(--blue)"><svg width="16" height="20" viewBox="0 0 16 20"><path d="M8 0a7 7 0 0 0-7 7c0 5 7 13 7 13s7-8 7-13a7 7 0 0 0-7-7z" fill="#fff"/><circle cx="8" cy="7" r="2.5" fill="#4a86e0"/></svg></div>
    <h4>Brindle Cove Optometry</h4>
    <div class="addr">4410 Marlowe Blvd, Fernbrook,<br>CA 91900, USA</div>
    <div class="lines">e. info@brindlecove.com<br>Call. 818 . 555 . 0142<br>F. 818 . 555 . 0143</div>
    <div class="pill">View Map</div>
  </div>
  <div class="fcol">
    <div class="pin" style="background:var(--white)"><svg width="16" height="20" viewBox="0 0 16 20"><path d="M8 0a7 7 0 0 0-7 7c0 5 7 13 7 13s7-8 7-13a7 7 0 0 0-7-7z" fill="#4a86e0"/><circle cx="8" cy="7" r="2.5" fill="#fff"/></svg></div>
    <h4>Willow Ridge</h4>
    <div class="addr">2281 Alder Crest St, Willow Ridge,<br>CA 91902, USA</div>
    <div class="lines">e. willowridge@brindlecove.com<br>Call. 818 . 555 . 0177<br>F.</div>
    <div class="pill">View Map</div>
  </div>
  <div class="fcol">
    <h4>Get in Touch</h4>
    <div class="socials"><i style="background:#4e64b0"></i><i style="background:#d5463a"></i><i style="background:#2f8fb8"></i><i style="background:#dd4b39"></i></div>
    <div class="contact-link">Contact Us</div>
  </div>
</footer>

</body>
</html>
```